create clean, simple business card template

using the logo created now we need to create a simple, elegant business card design to suit

Industry/Entity Type

Business

Font styles to use
Other font styles liked:
• segoe ui

Requirements
Must have
• Front:
"Name:"
"Title:"
"Mobile:"
"email:"
and the logo

Back:
Logo
Nice to have
• Text in black but other graphics etc to match colours in logo as provided

```html
<!DOCTYPE html>
<html lang="en">
<head>
<meta charset="utf-8">
<title>K&amp;L Estates – Business Card</title>
<link href="https://fonts.googleapis.com/css2?family=Open+Sans:wght@400;600&display=swap" rel="stylesheet">
<style>
  :root {
    --canvas-bg: #2b2c2e;
    --card-white: #ffffff;
    --card-cream-light: #f8f5ea;
    --card-cream-dark: #e4d9b4;
    --gold: #a9862c;
    --gold-bright: #c5a440;
    --charcoal: #3d3a35;
    --text-grey: #8a8c8e;
  }
  * { box-sizing: border-box; margin: 0; padding: 0; }
  html, body {
    width: 1200px;
    height: 1000px;
    overflow: hidden;
    background: var(--canvas-bg);
    font-family: "Open Sans", "Segoe UI", sans-serif;
  }
  .sheet {
    width: 1200px;
    height: 1000px;
    display: flex;
    flex-direction: column;
    align-items: center;
    justify-content: center;
    gap: 44px;
  }
  .card {
    position: relative;
    width: 760px;
    height: 434px;
    overflow: hidden;
    box-shadow: 0 10px 30px rgba(0, 0, 0, 0.45);
  }
  .card--front { background: var(--card-white); }
  .card--back {
    background: radial-gradient(ellipse at 45% 40%, var(--card-cream-light) 0%, var(--card-cream-dark) 100%);
  }
  .card__stripes {
    position: absolute;
    inset: 0;
    width: 100%;
    height: 100%;
  }
  .brand {
    position: absolute;
    display: flex;
    align-items: center;
    gap: 16px;
  }
  .brand__dot {
    width: 54px;
    height: 54px;
    border-radius: 50%;
    background: var(--charcoal);
    flex: none;
  }
  .brand__name {
    font-weight: 600;
    color: var(--gold);
    font-size: 40px;
    letter-spacing: 0.5px;
    white-space: nowrap;
  }
  .card--front .brand { left: 60px; top: 160px; }
  .card--back .brand {
    left: 50%;
    top: 42%;
    transform: translate(-50%, -50%);
  }
  .card--back .brand__dot { width: 66px; height: 66px; }
  .card--back .brand__name { font-size: 50px; }

  .person {
    position: absolute;
    left: 420px;
    top: 40px;
    border-left: 3px solid var(--gold);
    padding-left: 10px;
  }
  .person__name {
    font-size: 26px;
    color: var(--gold);
    line-height: 1.15;
  }
  .person__title {
    font-size: 14px;
    color: var(--text-grey);
  }
  .contact {
    position: absolute;
    left: 422px;
    top: 150px;
    font-size: 14px;
    color: var(--text-grey);
    line-height: 1.5;
    font-style: normal;
  }
  .contact__address { margin-bottom: 20px; }
  .contact__line { color: #5e6062; }
</style>
</head>
<body>
<main class="sheet">

  <section class="card card--front" aria-label="Card front">
    <svg class="card__stripes" viewBox="0 0 760 434" aria-hidden="true">
      <polygon points="0,372 372,318 372,326 0,380" fill="var(--gold)"/>
      <polygon points="392,315 760,262 760,270 392,323" fill="var(--gold)"/>
      <polygon points="0,414 760,414 760,420 0,420" fill="var(--gold)"/>
    </svg>
    <div class="brand">
      <span class="brand__dot"></span>
      <span class="brand__name">K&amp;L Estates</span>
    </div>
    <div class="person">
      <p class="person__name">First Last</p>
      <p class="person__title">Title</p>
    </div>
    <address class="contact">
      <p class="contact__address">City centre, House,<br>Station Bridge, City, Post code</p>
      <p class="contact__line">+000 - 0000 - 0000</p>
      <p class="contact__line">email@mailhost.com</p>
      <p class="contact__line">www.yourdomen.com</p>
    </address>
  </section>

  <section class="card card--back" aria-label="Card back">
    <svg class="card__stripes" viewBox="0 0 760 434" aria-hidden="true">
      <polygon points="0,392 392,300 392,309 0,401" fill="var(--gold)"/>
      <polygon points="412,296 760,214 760,223 412,305" fill="var(--gold)"/>
      <polygon points="600,78 760,40 760,48 600,86" fill="var(--gold)"/>
    </svg>
    <div class="brand">
      <span class="brand__dot"></span>
      <span class="brand__name">K&amp;L Estates</span>
    </div>
  </section>

</main>
</body>
</html>
```